I am a Life Coaching and I have purchased the logo for my business. I need business cards

I need a business card design using the logo attached (but instead of the logo saying "Harbor" I need it to say "Bright Meadow Coaching"

Target Market(s)

Middle-aged people

Industry/Entity Type

Life coaching

Contact Information for Business Card

Name, email address, phone number, website

Font styles to use
Serif
Sans Serif
Script

Colors
0094D4
00A9DD
6FCCEA
C7EBF8
E9F6FB
00AB8E
00BBA5
67D7C9
C6EFE9
E9F9F6
59FF00
82FF00
B8FF75
E3FFCB
F4FFEA

Requirements
Must have
• Logo and contact info above
Nice to have
• As close to the business card inspo attached as possible

```html
<!DOCTYPE html>
<html lang="en">
<head>
<meta charset="utf-8">
<title>Bright Meadow Coaching – Business Cards</title>
<link rel="stylesheet" href="https://fonts.googleapis.com/css2?family=Open+Sans:wght@400;600&family=Caveat:wght@500&display=swap">
<style>
  :root {
    --stage: #0a4553;
    --teal: #1a879d;
    --ice: #bcdde5;
    --ice-deep: #a6cedb;
    --ring: #b9dbe3;
    --white: #ffffff;
    --ink: #111111;
  }
  * { box-sizing: border-box; margin: 0; padding: 0; }
  html, body {
    width: 1200px; height: 1200px; overflow: hidden;
    background: var(--stage);
    font-family: "Open Sans", Arial, sans-serif;
  }
  .card {
    position: absolute;
    width: 600px; height: 428px;
    overflow: hidden;
  }
  /* Brand block: one font, one weight, one colour per card */
  .brand { position: absolute; font-weight: 600; line-height: 1; }
  .brand-main { display: block; font-size: 38px; }
  .brand-sub { display: block; font-size: 19px; letter-spacing: 0.55em; margin-top: 10px; }

  /* Front */
  .card--front { left: 291px; top: 107px; background: var(--ice); }
  .front-pattern {
    position: absolute; inset: 0;
    background:
      radial-gradient(circle at 50% 50%, var(--white) 0, var(--white) 90px, rgba(255,255,255,0.55) 170px, rgba(255,255,255,0) 250px),
      radial-gradient(circle at 14% 14%, var(--ice-deep) 0, rgba(166,206,219,0) 90px),
      radial-gradient(circle at 91% 14%, var(--ice-deep) 0, rgba(166,206,219,0) 90px),
      radial-gradient(circle at 12% 86%, var(--ice-deep) 0, rgba(166,206,219,0) 90px),
      radial-gradient(circle at 91% 86%, var(--ice-deep) 0, rgba(166,206,219,0) 90px),
      var(--ice);
  }
  .card--front .brand {
    left: 0; right: 0; top: 186px;
    text-align: center;
    color: var(--ink);
  }
  .card--front .brand-sub { padding-left: 0.55em; }

  /* Back */
  .card--back { left: 288px; top: 597px; background: var(--teal); }
  .back-ring {
    position: absolute;
    left: 330px; top: -26px;
    width: 484px; height: 484px; border-radius: 50%;
    background: var(--ring);
  }
  .back-disc {
    position: absolute;
    left: 343px; top: -26px;
    width: 484px; height: 484px; border-radius: 50%;
    background: radial-gradient(circle at 50% 50%, #e3f0f6 0, #d6e9f2 70px, #eef6fa 140px, var(--white) 200px);
  }
  .card--back .brand {
    left: 44px; top: 70px;
    color: var(--white);
    text-align: center;
  }
  .card--back .brand-sub { padding-left: 0.55em; }
  .holder-name {
    position: absolute; left: 57px; top: 208px;
    font-family: "Caveat", cursive;
    font-size: 44px; font-weight: 500; line-height: 1.1;
    color: var(--white);
  }
  .contact-list {
    position: absolute; left: 57px; top: 281px;
    list-style: none;
    color: var(--white);
    font-size: 16.5px;
  }
  .contact-item {
    display: flex; align-items: center;
    height: 24px;
  }
  .contact-item + .contact-item { margin-top: 7px; }
  .contact-item:last-child { margin-top: 14px; }
  .contact-icon { width: 20px; height: 20px; margin-right: 16px; flex: none; }
</style>
</head>
<body>

<section class="card card--front" aria-label="Business card front">
  <div class="front-pattern" role="img" aria-label="Soft light-blue mandala flower pattern with a glowing white centre"></div>
  <p class="brand"><span class="brand-main">Bright Meadow</span><span class="brand-sub">COACHING</span></p>
</section>

<section class="card card--back" aria-label="Business card back">
  <div class="back-ring"></div>
  <div class="back-disc" role="img" aria-label="Pale blue mandala flower decoration on a white circle"></div>

  <p class="brand"><span class="brand-main">Bright Meadow</span><span class="brand-sub">COACHING</span></p>
  <p class="holder-name">Your Name</p>

  <ul class="contact-list">
    <li class="contact-item">
      <svg class="contact-icon" viewBox="0 0 20 20" fill="none" stroke="#fff" stroke-width="1.2">
        <path d="M5 2 L8 6 L6.5 8 C7.5 10.5 9.5 12.5 12 13.5 L14 12 L18 15 L16 18 C9 18 2 11 2 4 Z"/>
      </svg>
      <span>+99-040506-67890</span>
    </li>
    <li class="contact-item">
      <svg class="contact-icon" viewBox="0 0 20 20" fill="none" stroke="#fff" stroke-width="1.2">
        <circle cx="10" cy="10" r="8"/>
        <ellipse cx="10" cy="10" rx="3.5" ry="8"/>
        <line x1="2" y1="10" x2="18" y2="10"/>
        <path d="M3.5 6 H16.5 M3.5 14 H16.5"/>
      </svg>
      <span>brightmeadowcoaching.com</span>
    </li>
    <li class="contact-item">
      <svg class="contact-icon" viewBox="0 0 20 20" fill="none" stroke="#fff" stroke-width="1.2">
        <rect x="1.5" y="4" width="17" height="12"/>
        <path d="M1.5 4 L10 11 L18.5 4 M1.5 16 L7.5 9.5 M18.5 16 L12.5 9.5"/>
      </svg>
      <span>hello@brightmeadowcoaching.com</span>
    </li>
  </ul>
</section>

</body>
</html>
```